Catalog copying current designs, web designs and copywrite.

I am looking for someone to recreate a draft catalog using the same design process.

My entire brief with the photo samples and icons would not fit in here. They are in the google docs folder as below:

https://share.plovimbox.net/folders/7hQwRk2mZaXe9TnB4LpYcVd3sUfGj6K?mode=view

```html
<!DOCTYPE html>
<html lang="en">
<head>
<meta charset="UTF-8">
<title>Prime Select – About Us &amp; Our Process</title>
<link rel="stylesheet" href="https://fonts.googleapis.com/css2?family=Archivo+Black&family=Arimo:wght@400;700&display=swap">
<style>
  :root {
    --backdrop: #e4e4e4;
    --paper: #f2f2f2;
    --paper-shade: #d9d9d9;
    --ink: #2b2b2b;
    --ink-soft: #555555;
    --accent: #8c1b22;
    --label-grey: #b9b9b9;
    --white: #ffffff;
  }
  * { box-sizing: border-box; margin: 0; padding: 0; }
  html, body {
    width: 1200px; height: 900px; overflow: hidden;
    background: var(--backdrop);
  }
  .spread {
    position: absolute; left: 180px; top: 153px;
    width: 840px; height: 594px; display: flex;
    box-shadow: 0 18px 40px rgba(0,0,0,0.18);
  }
  .page {
    position: relative; width: 420px; height: 594px; overflow: hidden;
    font-family: "Arimo", Arial, sans-serif; color: var(--ink);
  }
  .page-texture {
    position: absolute; inset: 0;
    background:
      linear-gradient(135deg, rgba(255,255,255,0.7) 0%, rgba(255,255,255,0) 45%),
      linear-gradient(200deg, var(--paper-shade) 0%, var(--paper) 55%, var(--paper-shade) 100%);
  }
  .page--left .page-texture::after,
  .page--right .page-texture::after {
    content: ""; position: absolute; top: 0; bottom: 0; width: 40px;
  }
  .page--left .page-texture::after { right: 0; background: linear-gradient(90deg, rgba(0,0,0,0), rgba(0,0,0,0.12)); }
  .page--right .page-texture::after { left: 0; background: linear-gradient(90deg, rgba(0,0,0,0.12), rgba(0,0,0,0)); }

  .section-label {
    position: absolute; left: 14px; top: 22px;
    writing-mode: vertical-rl; transform: rotate(180deg);
    font-family: "Archivo Black", Arial, sans-serif;
    font-size: 34px; letter-spacing: 1px; color: var(--label-grey);
  }
  .display {
    font-family: "Archivo Black", Arial, sans-serif;
    text-transform: uppercase; line-height: 0.95;
  }
  .headline { position: absolute; left: 64px; top: 108px; }
  .headline .kicker { color: var(--accent); font-size: 13px; margin: 3px 0 3px; }
  .headline .main { color: var(--ink); font-size: 28px; }

  .body-copy { font-size: 8.5px; line-height: 1.45; color: var(--ink-soft); text-align: justify; }
  .intro { position: absolute; left: 222px; top: 294px; width: 178px; }
  .values {
    position: absolute; left: 196px; top: 392px; width: 206px;
    display: flex; justify-content: space-between; list-style: none;
  }
  .value { width: 64px; text-align: center; line-height: 1; }
  .value svg { width: 24px; height: 24px; display: block; margin: 0 auto 5px; }
  .value span {
    display: block;
    font-family: "Arimo", Arial, sans-serif; font-weight: 700;
    font-size: 6.5px; color: var(--accent); text-transform: uppercase; line-height: 1.25;
  }
  .mission { position: absolute; left: 196px; top: 452px; width: 206px; }

  .folio { position: absolute; left: 0; bottom: 36px; width: 30px; height: 30px; }
  .folio svg { width: 30px; height: 30px; }
  .folio span { position: absolute; left: 5px; top: 8px; font-size: 10px; line-height: 1; color: var(--ink-soft); }

  .process-title { position: absolute; left: 70px; top: 112px; font-size: 40px; color: var(--ink); }
  .steps { position: absolute; left: 62px; top: 228px; width: 320px; list-style: none; }
  .step { display: flex; gap: 14px; margin-bottom: 30px; }
  .step-number {
    font-family: "Archivo Black", Arial, sans-serif;
    font-size: 46px; line-height: 1; color: var(--accent); width: 36px; flex: none;
  }
  .step-title {
    font-family: "Archivo Black", Arial, sans-serif;
    font-size: 12px; color: var(--accent); text-transform: uppercase; margin: 4px 0 5px;
  }
  .step .body-copy { width: 250px; }
</style>
</head>
<body>
  <main class="spread">
    <section class="page page--left">
      <div class="page-texture" role="img" aria-label="Soft grey low-poly faceted background"></div>
      <h2 class="section-label">About Us</h2>
      <h1 class="headline display">
        <div class="kicker">Industry Leading</div>
        <div class="main">Recruitment<br>&amp; Labour<br>Hire</div>
        <div class="kicker">Agency In</div>
        <div class="main">New South<br>Wales</div>
      </h1>
      <p class="intro body-copy">At Prime Select, we're all about ensuring our clients achieve their goals and success in their field. This is why we focus on providing qualified workers for their business. Make us your partner and watch these goals turned into action.</p>
      <ul class="values">
        <li class="value">
          <svg viewBox="0 0 26 26" fill="none" stroke="var(--accent)" stroke-width="1.6" stroke-linecap="round">
            <path d="M9 16c-2-1.6-3-3.4-3-5.6a7 7 0 0 1 14 0c0 2.2-1 4-3 5.6v2H9z"/>
            <path d="M10 21h6M11 24h4M13 1v2M3 4l1.5 1.5M23 4l-1.5 1.5"/>
          </svg>
          <span>Inspiring<br>Others</span>
        </li>
        <li class="value">
          <svg viewBox="0 0 26 26" fill="none" stroke="var(--accent)" stroke-width="1.6" stroke-linecap="round">
            <circle cx="12" cy="14" r="10"/><circle cx="12" cy="14" r="6"/><circle cx="12" cy="14" r="2"/>
            <path d="M12 14l11-11M19 3h4v4"/>
          </svg>
          <span>Achieving<br>Goals</span>
        </li>
        <li class="value">
          <svg viewBox="0 0 26 26" fill="var(--accent)">
            <rect x="9" y="12" width="8" height="13"/><rect x="1" y="17" width="7" height="8"/><rect x="18" y="19" width="7" height="6"/>
            <circle cx="13" cy="4" r="2.5"/><path d="M10 11l1-4h4l1 4z"/>
          </svg>
          <span>Driven<br>To Succeed</span>
        </li>
      </ul>
      <p class="mission body-copy">We are extremely passionate about what we do and take pride in our excellence in the Labour Hire industry. We look to give our clients the best service possible. We want every worker we place to feel valued and supported. Let us become your trusted Labour Hire company.</p>
      <div class="folio">
        <svg viewBox="0 0 30 30"><path d="M0 0L30 15L0 30z" fill="var(--white)"/></svg>
        <span>2</span>
      </div>
    </section>

    <section class="page page--right">
      <div class="page-texture" role="img" aria-label="Soft grey low-poly faceted background"></div>
      <h2 class="section-label">Why Us?</h2>
      <h2 class="process-title display">Our<br>Process</h2>
      <ol class="steps">
        <li class="step">
          <div class="step-number">1</div>
          <div>
            <h3 class="step-title">Initiation</h3>
            <p class="body-copy">Prime Select initially engages with the employer to create a trusted relationship. We understand the clients' needs and assign appropriate resources to forward our services.</p>
          </div>
        </li>
        <li class="step">
          <div class="step-number">2</div>
          <div>
            <h3 class="step-title">Assessment</h3>
            <p class="body-copy">We assess the employers' criteria and hand over the appropriate candidates for the job. Unlike most recruitment companies, we do not just send a bunch of resumes, but rather ensure that we are sending the greatest quality candidates that best meet their needs.</p>
          </div>
        </li>
        <li class="step">
          <div class="step-number">3</div>
          <div>
            <h3 class="step-title">Placement</h3>
            <p class="body-copy">Employers then interview the candidates put forward by Prime Select in order to fill the vacancy and ensure that the candidate is the best fit for their position.</p>
          </div>
        </li>
      </ol>
    </section>
  </main>
</body>
</html>
```